1 Page Website Design For Diabetic Discount RX Card

~~I NEED A WEBSITE LANDING PAGE DESIGNED~~:

TITLE: GET UP TO 75% Off ALL YOUR DIABETIC SUPPLIES GUARANTEED
SUBITITLE: Never Pay Full Price For Your Diabetic Supplies Again!

~~FORM~~:
Choose Your Current Brand Of Diabetic Supplies That You Currently Use To See If They Are Covered Under Our Free Diabetic RX Assistance Program:

~~DROP DOWN MENU~~
Acarbose Up To 75% Off!

Zernovab Tel Up To 75% Off!

Zernovab Tel Xr Up To 54% Off!

Wempu Up To 75% Off!

Orvantel Up To 75% Off!

Quilmor Up To 75% Off!

Tesfunn Up To 75% Off!

Wombeth Up To 75% Off!

Elkrostiv Up To 54% Off!

Irmoskuve Up To 54% Off!

Ulpremo Up To 54% Off!

Fashkelin Up To 75% Off!

Kolvrin Up To 75% Off!

Chlorpropamide Up To 75% Off!

Colesevelam Up To 75% Off!

Pembrath Up To 54% Off!

Qwemt Up To 75% Off!

Desmopressin 52% Off

Sornefil 74% Off

Ferlutham Up To 54% Off!
Mirsolk Up To 75% Off!

Kelmuro Up To 75% Off!

Yibrosel Up To 75% Off!

Glimepiride 66% Off

Glipizide Up To 75% Off!

Glipizide Er Up To 75% Off!

Ventrosimel Up To 75% Off!

Ventrosimel Xr Up To 75% Off!

Brastumol Up To 75% Off!

Brastumol Xl Up To 75% Off!

Pelkirona Up To 75% Off!

Sovrinka Up To 75% Off!

Glyburide Up To 75% Off!

Glyburide Micronized Up To 75% Off!
Twerdo Up To 75% Off!

Omrick Up To 75% Off!

Hestrolu Up To 75% Off!

Pirvetan 50 50 Up To 75% Off!

Pirvetan Up To 75% Off!

Vostrek N Up To 75% Off!

Vostrek R Up To 75% Off!

Insulin Detemir Up To 75% Off!

Insulin Glulisine Up To 75% Off!

Selbrudar Up To 75% Off!

Thebrisu Up To 75% Off!

Kwelbor Up To 75% Off!

Kwelbor Xr Up To 75% Off!

Mostrelo Up To 75% Off!

Pelvouste Up To 75% Off!

Wurmbostel Up To 75% Off!

Trevlu Up To 75% Off!

Hustravel Xr Up To 75% Off!

Privok Up To 75% Off!

Dosharp Up To 75% Off!

Ostrubel Up To 54% Off!

Metformin 73% Off

Talverush Up To 54% Off!

Miglitol Up To 75% Off!

Skevrant Up To 33% Off!

Nateglinide Up To 75% Off!

Wolbrey Up To 75% Off!

Piltrago Up To 75% Off!

Kestrub N Up To 75% Off!

Kestrub R Up To 75% Off!

Harpenu Up To 75% Off!

Blemkarsu Up To 33% Off!

Skirvet Up To 75% Off!

Plembuth Up To 54% Off!

Vurlk Up To 75% Off!

Pioglitazone Up To 75% Off!

Pramlintide Up To 75% Off!

Welhostro Up To 54% Off!

Kuvelst Up To 75% Off!

Dimbrul 20% Off

Repaglinide Up To 75% Off!

Sklavon Up To 75% Off!

Rosiglitazone Up To 75% Off!

Sitagliptin Up To 75% Off!

Humbrev Up To 75% Off!

Fortkavul Up To 75% Off!

Pelbruko Up To 75% Off!

Wiskorb Up To 75% Off!

Tolazamide Up To 75% Off!

Tolbutamide Up To 75% Off!

Breshmuv Up To 54% Off!

Skamvi Up To 75% Off!

Huvelpsor Up To 75% Off!

Komplev Up To 75% Off!

Skyvelmon Up To 15% Off!

Bospenarve Up To 75% Off!

Fresvomel Up To 33% Off!

Drumpal Up To 75% Off!

Spirnak Up To 75% Off!

Premvol Xr Up To 75% Off!

~~~~After they choose one I want this message to pop up~~~~:

YES! ~~NAME OF DRUG~~ IS COVERED UNDER OUR FREE DIABETIC RX PROGRAM!
3 EASY WAYS TO RECEIVE YOUR FREE DIABETIC RX ASSISTANCE VOUCHER:

1. Simply Click Below To Download Your Voucher Right Now!

~~DOWNLOAD VOUCHER NOW~~
2. Enter Your Cell Phone Number And We Will Send The Voucher To You By Text Message Instantly:

3. Enter Your Email And We Will Send The Voucher To Your Email Instantly:

Target Market(s)

People with Diabetes

Number of Pages Required

1 page

Colors

Designer to choose colors to be used in the design.

Requirements
Must have
• must be professional looking and build trust and credibility
Nice to have
• Photos of diabetics...real people
Should not have
• red

```html
<!DOCTYPE html>
<html lang="en">
<head>
<meta charset="utf-8">
<title>Diabetic RX Assistance Program</title>
<link href="https://fonts.googleapis.com/css2?family=Lato:wght@400;700;900&family=Open+Sans:wght@400;600;700;800&display=swap" rel="stylesheet">
<style>
:root{
  --nav:#263547;
  --nav-active:#34506b;
  --orange:#f39c12;
  --blue:#0a6ebd;
  --navy:#0b4c7c;
  --hero:#5d9fd2;
  --text:#333b44;
  --muted:#6d7680;
  --line:#e3e6ea;
  --footer:#f4f6f8;
  --white:#ffffff;
}
*{box-sizing:border-box;margin:0;padding:0}
html,body{width:1200px;height:2575px;overflow:hidden}
body{position:relative;background:var(--white);font-family:"Lato",Arial,sans-serif;color:var(--text)}
.abs{position:absolute}

/* nav */
.site-nav{left:0;top:0;width:1200px;height:55px;background:var(--nav)}
.site-nav .brand{left:107px;top:10px;font-size:30px;font-weight:700;color:var(--white);letter-spacing:1px}
.nav-links{right:95px;top:0;display:flex;height:55px}
.nav-links a{display:flex;align-items:center;padding:0 18px;color:var(--white);font-size:14px;font-weight:700;text-decoration:none;height:55px}
.nav-links a.active{background:var(--nav-active);border-top:3px solid var(--orange)}

/* hero */
.hero{left:0;top:55px;width:1200px;height:518px;background:linear-gradient(100deg,#7fb6e0 0%,#5d9fd2 45%,#4c8fc6 100%)}
.hero-title{left:0;top:178px;width:1200px;text-align:center;font-family:"Open Sans",sans-serif;font-weight:800;font-size:31px;color:var(--white);letter-spacing:.5px}
.hero-sub{left:0;top:218px;width:1200px;text-align:center;font-size:23px;color:var(--white)}
.hero-btn{top:285px;width:164px;height:44px;border-radius:22px;display:flex;align-items:center;justify-content:center;color:var(--white);font-weight:700;font-size:15px;box-shadow:0 3px 0 rgba(0,0,0,.15)}
.hero-btn.start{left:433px;background:var(--blue)}
.hero-btn.learn{left:605px;background:var(--orange)}
.hero-dots{left:578px;top:480px;display:flex;gap:5px}
.hero-dots span{width:7px;height:7px;border-radius:50%;background:rgba(255,255,255,.5)}
.hero-dots span:first-child{background:var(--white)}

/* intro */
.intro-star{left:585px;top:610px}
.intro-text{left:0;top:648px;width:1200px;text-align:center;font-family:"Open Sans",sans-serif;font-size:19px;line-height:28px;color:var(--muted)}
.intro-text .link-blue{color:#3f8fd0}
.intro-text .link-orange{color:var(--orange)}

/* brand list */
.brand-list{left:107px;top:818px;list-style:none;font-family:"Open Sans",sans-serif;font-size:15px;color:var(--muted)}
.brand-list li{height:53.7px}
.brand-list li.selected{color:#1d2733;font-weight:700}
.brand-list li.selected em{font-style:normal;color:var(--orange)}
.see-more{left:107px;top:1672px;font-family:"Open Sans",sans-serif;font-size:14px;color:#1d2733;text-decoration:underline}
.list-divider{left:425px;top:810px;width:2px;height:888px;background:var(--line)}

/* coverage panel */
.coverage-head{left:473px;top:836px;width:632px;text-align:center;font-family:"Open Sans",sans-serif;font-weight:600;font-size:15.5px;line-height:25px;color:#1d2733}
.coverage-head b{color:#1d2733;font-weight:800}
.rule{left:473px;width:632px;height:1px;background:var(--line)}
.step-label{left:473px;width:632px;text-align:center;font-family:"Open Sans",sans-serif;font-size:11px;color:var(--muted)}
.download-btn{left:611px;top:994px;width:367px;height:44px;border-radius:22px;background:var(--orange);box-shadow:0 3px 0 rgba(0,0,0,.15);display:flex;align-items:center;justify-content:center;gap:10px;color:var(--white);font-weight:700;font-size:15px;letter-spacing:.5px}
.send-field{left:612px;width:366px;height:43px;border-radius:22px;background:var(--white);box-shadow:0 2px 6px rgba(0,0,0,.18)}
.send-field .placeholder{position:absolute;left:40px;top:13px;font-family:"Open Sans",sans-serif;font-size:12px;color:var(--muted)}
.send-field .send{position:absolute;right:0;top:0;width:110px;height:43px;border-radius:22px;background:var(--navy);display:flex;align-items:center;justify-content:center;gap:7px;color:var(--white);font-weight:700;font-size:15px}

/* testimonial */
.quote-mark{left:838px;top:1535px;font-family:"Open Sans",sans-serif;font-size:60px;color:#e2e5e8;line-height:1}
.testimonial-quote{right:40px;top:1538px;font-family:"Open Sans",sans-serif;font-size:22px;color:#1d2733}
.testimonial-name{right:40px;top:1573px;font-family:"Open Sans",sans-serif;font-size:16px;color:var(--text)}
.testimonial-dots{right:57px;top:1626px;display:flex;gap:4px}
.testimonial-dots span{width:8px;height:8px;border-radius:50%;background:#d5d8dc}
.testimonial-dots span:first-child{background:#444}
.people-photo{left:476px;top:1595px;width:724px;height:185px;background:linear-gradient(180deg,#f3ece6 0%,#e4cdb9 50%,#c9a58a 100%)}

/* cta */
.cta-band{left:0;top:1780px;width:1200px;height:382px;background:linear-gradient(180deg,#9a7258 0%,#8b6d5e 55%,#6f6e78 100%)}
.cta-title{left:0;top:1870px;width:1200px;text-align:center;font-size:37px;font-weight:700;color:var(--white)}
.cta-btn{left:392px;top:1950px;width:417px;height:65px;border-radius:33px;background:var(--white);display:flex;align-items:center;justify-content:center;font-size:18px;font-weight:900;letter-spacing:1px;color:#1d2733}

/* footer */
.site-footer{left:0;top:2162px;width:1200px;height:413px;background:var(--footer)}
.footer-brand{left:138px;top:2218px;font-size:32px;font-weight:700;color:#1d2733}
.footer-about{left:138px;top:2276px;width:290px;font-family:"Open Sans",sans-serif;font-size:12px;line-height:16px;letter-spacing:.6px;color:var(--muted)}
.social{left:138px;top:2382px;display:flex;gap:7px}
.social span{width:22px;height:22px;background:#1d2733}
.social span:first-child{background:var(--orange)}
.footer-col{top:2226px}
.footer-col h4{font-size:19px;font-weight:400;color:#1d2733;margin-bottom:20px}
.footer-col ul{list-style:none;font-family:"Open Sans",sans-serif;font-size:12.5px;color:var(--muted)}
.footer-col li{height:48px}
.footer-bottom-rule{left:0;top:2528px;width:1200px;height:1px;background:var(--line)}
.copyright{left:138px;top:2545px;font-family:"Open Sans",sans-serif;font-size:12.5px;color:var(--muted)}
.copyright u{color:var(--muted)}
</style>
</head>
<body>

<header class="abs site-nav">
  <div class="abs brand">LOGO</div>
  <nav class="abs nav-links">
    <a class="active">Home</a><a>Menu</a><a>Page</a><a>About</a><a>Contact</a>
  </nav>
</header>

<section class="abs hero" role="img" aria-label="Smiling senior man speaking with a doctor, blue tinted photo"></section>
<h1 class="abs hero-title">GET UP TO 75% Off ALL YOUR DIABETIC SUPPLIES GUARANTEED</h1>
<p class="abs hero-sub">Never Pay Full Price For Your Diabetic Supplies Again!</p>
<div class="abs hero-btn start">START NOW</div>
<div class="abs hero-btn learn">LEARN MORE</div>
<div class="abs hero-dots"><span></span><span></span><span></span><span></span></div>

<svg class="abs intro-star" width="30" height="30" viewBox="0 0 24 24"><path fill="#c8ccd0" d="M12 1.5l3.2 6.9 7.4.8-5.5 5 1.6 7.4L12 17.8l-6.7 3.8 1.6-7.4-5.5-5 7.4-.8z"/></svg>
<p class="abs intro-text">Choose your current brand of <span class="link-blue">Diabetic Supplies</span> that you currently use<br>to see if they are covered under our free <span class="link-orange">Diabetic RX Assistance Program:</span></p>

<ul class="abs brand-list">
  <li class="selected">Acarbose Up To <em>75%</em> Off!</li>
  <li>Zernovab Tel Up To 75% Off!</li>
  <li>Zernovab Tel Xr Up To 54% Off!</li>
  <li>Wempu Up To 75% Off!</li>
  <li>Orvantel Up To 75% Off!</li>
  <li>Quilmor Up To 75% Off!</li>
  <li>Tesfunn Up To 75% Off!</li>
  <li>Wombeth Up To 75% Off!</li>
  <li>Elkrostiv Up To 54% Off!</li>
  <li>Irmoskuve Up To 54% Off!</li>
  <li>Ulpremo Up To 54% Off!</li>
  <li>Fashkelin Up To 75% Off!</li>
  <li>Kolvrin Up To 75% Off!</li>
  <li>Chlorpropamide Up To 75% Off!</li>
  <li>Colesevelam Up To 75% Off!</li>
  <li>Pembrath Up To 54% Off!</li>
</ul>
<div class="abs see-more">see 27+ more &gt;&gt;</div>
<div class="abs list-divider"></div>

<div class="abs coverage-head">YES! <b>ACARBOSE</b> IS COVERED UNDER OUR FREE DIABETIC RX PROGRAM!<br>3 EASY WAYS TO RECEIVE YOUR FREE DIABETIC RX ASSISTANCE VOUCHER:</div>
<div class="abs rule" style="top:924px"></div>
<p class="abs step-label" style="top:958px">1. Simply Click Below To Download Your Voucher Right Now!</p>
<div class="abs download-btn">
  <svg width="16" height="16" viewBox="0 0 16 16"><path fill="#fff" d="M6 1h4v6h3l-5 5-5-5h3zM1 13h14v2H1z"/></svg>
  DOWNLOAD
</div>
<div class="abs rule" style="top:1090px"></div>
<p class="abs step-label" style="top:1131px">2. Enter Your Cell Phone Number And We Will Send The Voucher To You By Text Message Instantly:</p>
<div class="abs send-field" style="top:1187px">
  <span class="placeholder">Enter phone here</span>
  <span class="send"><svg width="14" height="14" viewBox="0 0 14 14"><circle cx="7" cy="7" r="6" fill="none" stroke="#fff" stroke-width="1.6"/><path d="M4 7h6M7.5 4.5L10 7 7.5 9.5" fill="none" stroke="#fff" stroke-width="1.6"/></svg>SEND</span>
</div>
<div class="abs rule" style="top:1272px"></div>
<p class="abs step-label" style="top:1305px">3. Enter Your Email And We Will Send The Voucher To Your Email Instantly:</p>
<div class="abs send-field" style="top:1361px">
  <span class="placeholder">Enter phone here</span>
  <span class="send"><svg width="14" height="14" viewBox="0 0 14 14"><circle cx="7" cy="7" r="6" fill="none" stroke="#fff" stroke-width="1.6"/><path d="M4 7h6M7.5 4.5L10 7 7.5 9.5" fill="none" stroke="#fff" stroke-width="1.6"/></svg>SEND</span>
</div>
<div class="abs rule" style="top:1447px"></div>

<div class="abs quote-mark">&#8221;</div>
<p class="abs testimonial-quote">‘It was amazing using this voucher!’</p>
<p class="abs testimonial-name">Dessa, Texas IL</p>
<div class="abs testimonial-dots"><span></span><span></span><span></span><span></span><span></span><span></span><span></span></div>
<div class="abs people-photo" role="img" aria-label="Group of smiling people photographed together"></div>

<section class="abs cta-band" role="img" aria-label="Person holding a glucose meter, warm tinted photo"></section>
<h2 class="abs cta-title">Never Pay Full Price For Your Diabetic Supplies Again!</h2>
<div class="abs cta-btn">GET YOUR VOUCHER TODAY!</div>

<footer class="abs site-footer"></footer>
<div class="abs footer-brand">LOGO</div>
<p class="abs footer-about">Lorem ipsum dolor sit amet, consertera consectetur adipisicing elit, sed do selle eiusmod tempor incididunt ut labore et dolore magna aliqua.</p>
<div class="abs social"><span></span><span></span><span></span></div>
<div class="abs footer-col" style="left:569px"><h4>Policy</h4><ul><li>Privacy Policy</li><li>Terms of Use</li><li>Contact Us</li><li>About us</li><li>Vouchers</li></ul></div>
<div class="abs footer-col" style="left:740px"><h4>About</h4><ul><li>About</li><li>Careers</li><li>Newsletter</li><li>Health Services</li><li>Accessibility</li></ul></div>
<div class="abs footer-col" style="left:924px"><h4>Vouchers</h4><ul><li>All Vouchers</li><li>Sales</li><li>New page</li><li>Health page</li><li>Accessibility</li></ul></div>
<div class="abs footer-bottom-rule"></div>
<p class="abs copyright">Copyright © 2008 - 2017 Company Name, LLC. All rights reserved. <u>See additional information.</u></p>

</body>
</html>
```